Direct Response Coupon/Flyer for Trade Show

We are looking for something simple and quick. Using our logo and maybe some stock photos.
We need a call to action piece with the following
1. " Every $5,000 save $1,000"
2. Limited time offer. Must reserve your procedure by June 15th
3. content is the following : KRVO is a medical tourism company that facilitates wellness by connecting our clients with qualified medical practitioners in Medellin, Colombia offering dental, vision, cosmetic and other medical procedures.
4. full color 3.5x8.25
5. On the bottom near the left or right we need "Member of the Global Care Travel Guild and the attached logo.
6. to speak to a case manger call 888-614-2073
7. our website is krvo-example.com to get an idea of our brand and style
looking for something quick
We want the same style as the attached brochure

```html
<!DOCTYPE html>
<html lang="en">
<head>
<meta charset="utf-8">
<title>KRVO Trade Show Flyer</title>
<link rel="stylesheet" href="https://fonts.googleapis.com/css2?family=Oswald:wght@300;400;500&display=swap">
<style>
  :root {
    --page-bg: #e4e5e7;
    --paper: #ffffff;
    --ink: #111111;
    --teal: #1a9ea6;
    --teal-dark: #138891;
    --black: #0b0b0b;
    --white: #ffffff;
    --gold: #c9a24a;
    --gold-dark: #8a6a24;
  }
  * { box-sizing: border-box; margin: 0; padding: 0; }
  html, body {
    width: 1200px; height: 1200px; overflow: hidden;
    background: var(--page-bg);
    font-family: "Oswald", sans-serif;
  }
  .flyer {
    position: absolute; left: 367px; top: 50px;
    width: 390px; height: 920px;
    transform: scale(1.1957); transform-origin: top left;
    background: linear-gradient(180deg, #ffffff 0%, #f4f4f4 100%);
    box-shadow: 0 4px 14px rgba(0,0,0,0.18);
    overflow: hidden;
  }
  .headline {
    position: absolute; left: 35px; right: 28px;
    color: var(--ink); font-weight: 500; line-height: 1;
    display: flex; justify-content: space-between; align-items: baseline;
  }
  .headline--save { top: 44px; font-size: 70px; }
  .headline--every { top: 130px; justify-content: flex-start; gap: 8px; }
  .headline__small { font-size: 38px; font-weight: 400; }
  .headline__big { font-size: 70px; }
  .journey { position: absolute; left: 0; top: 230px; width: 390px; height: 220px; }
  .offer {
    position: absolute; left: 40px; right: 20px; top: 466px;
    color: var(--teal); font-size: 21px; font-weight: 400;
    line-height: 33px; letter-spacing: 0.3px;
    text-align: justify; text-align-last: justify;
  }
  .offer sup { font-size: 12px; }
  .contact-band {
    position: absolute; left: 0; right: 0; top: 538px; height: 112px;
    background: linear-gradient(180deg, var(--teal) 0%, var(--teal-dark) 100%);
    color: var(--white); text-align: center;
    padding-top: 12px; font-size: 23px; line-height: 29px; font-weight: 400;
    letter-spacing: 0.3px;
  }
  .info-panel {
    position: absolute; left: 0; right: 0; top: 650px; bottom: 0;
    background: var(--black); color: var(--white);
  }
  .info-panel__text {
    position: absolute; left: 47px; right: 14px; top: 17px;
    font-size: 16.5px; line-height: 29px; font-weight: 400;
    text-align: justify;
  }
  .brand {
    position: absolute; left: 57px; top: 186px;
    display: flex; align-items: center; gap: 8px;
    color: var(--teal); font-size: 22px; font-weight: 400; letter-spacing: 1px;
  }
  .brand__dot {
    width: 14px; height: 14px; border-radius: 50%; background: var(--teal);
  }
  .membership {
    position: absolute; left: 212px; top: 176px;
    color: var(--gold); font-size: 11px; line-height: 19px; font-weight: 400;
    letter-spacing: 0.4px; text-transform: uppercase;
  }
  .membership__badge {
    position: absolute; left: 317px; top: 170px;
    width: 50px; height: 50px; border-radius: 50%;
    background: radial-gradient(circle at 40% 35%, var(--gold) 0%, var(--gold-dark) 100%);
  }
</style>
</head>
<body>
  <main class="flyer">
    <h1 class="headline headline--save"><span>Save</span><span>$1000</span></h1>
    <p class="headline headline--every"><span class="headline__small">for every</span><span class="headline__big">$5000</span></p>

    <svg class="journey" viewBox="0 0 390 220" aria-hidden="false">
      <defs>
        <linearGradient id="cityTone" x1="0" y1="0" x2="0" y2="1">
          <stop offset="0" stop-color="#9aa3ab"/>
          <stop offset="1" stop-color="#6f7460"/>
        </linearGradient>
        <linearGradient id="flightTone" x1="0" y1="0" x2="0" y2="1">
          <stop offset="0" stop-color="#7b8594"/>
          <stop offset="1" stop-color="#c7a27a"/>
        </linearGradient>
        <linearGradient id="clinicTone" x1="0" y1="0" x2="1" y2="1">
          <stop offset="0" stop-color="#e6ecee"/>
          <stop offset="1" stop-color="#9fb1b8"/>
        </linearGradient>
      </defs>
      <line x1="209" y1="65" x2="91" y2="157" stroke="var(--teal)" stroke-width="6"/>
      <line x1="209" y1="65" x2="314" y2="140" stroke="var(--teal)" stroke-width="6"/>
      <circle cx="209" cy="65" r="50" fill="url(#cityTone)" stroke="var(--teal)" stroke-width="7" role="img" aria-label="Photo of the Medellin city skyline"/>
      <circle cx="91" cy="157" r="50" fill="url(#flightTone)" stroke="var(--teal)" stroke-width="7" role="img" aria-label="Photo of a passenger jet taking off at sunset"/>
      <circle cx="314" cy="140" r="50" fill="url(#clinicTone)" stroke="var(--teal)" stroke-width="7" role="img" aria-label="Photo of a bright dental clinic treatment room"/>
    </svg>

    <p class="offer">Limited time offer. Must reserve<br>your procedure by June 15<sup>th</sup>.</p>

    <section class="contact-band">
      <p>TO SPEAK TO A CASE MANAGER</p>
      <p>CALL 888-614-2073</p>
      <p>or visit us at krvo-example.com</p>
    </section>

    <section class="info-panel">
      <p class="info-panel__text">KRVO is a medical tourism company that facilitates wellness by connecting our clients with qualified medical practitioners in Medellin, Colombia offering dental, vision, cosmetic and other medical procedures.</p>
      <div class="brand"><span class="brand__dot"></span><span>KRVO</span></div>
      <p class="membership">Member of the<br>Global Care<br>Travel Guild</p>
      <div class="membership__badge" role="img" aria-label="Guild membership badge"></div>
    </section>
  </main>
</body>
</html>
```